Flyer Template Design

I have attached 4 files. I would like a design template that could be used across these documents so that they have a common look and feel. The content of the documents is tested and should not be changed significantly. The images can be changed. I have also attache our logo for color compatibility.
Updates

Need extra days to review

Target Market(s)

Wealthy Christian donors

Font styles to use
Serif
Sans Serif

```html
<!DOCTYPE html>
<html lang="en">
<head>
<meta charset="utf-8">
<title>Harvest Trust – Brochure Spreads</title>
<link href="https://fonts.googleapis.com/css2?family=Libre+Baskerville:ital,wght@0,400;0,700;1,700&family=Open+Sans:ital,wght@0,400;0,700;1,400;1,700&display=swap" rel="stylesheet">
<style>
:root{
  --bg:#e4e5e7;
  --paper:#ffffff;
  --green:#1d4a2a;
  --green-dark:#173d22;
  --sky:#c3e2f1;
  --sky-soft:#d9eef7;
  --stripe:#8cc9e6;
  --ink:#2b2b2b;
  --accent:#3f9a7c;
}
*{box-sizing:border-box;margin:0;padding:0}
html,body{width:1200px;height:483px;overflow:hidden;background:var(--bg)}
body{position:relative;font-family:"Open Sans",Arial,sans-serif;color:var(--ink)}
.spread{position:absolute;display:flex;background:var(--paper);box-shadow:0 2px 8px rgba(0,0,0,.18)}
.spread--left{left:36px;top:38px;width:548px;height:412px}
.spread--right{left:610px;top:46px;width:558px;height:402px;border-top:6px solid var(--stripe)}
.panel{position:relative;height:100%;overflow:hidden}
.spread--left .panel{width:274px}
.spread--right .panel{width:279px}
.panel + .panel{border-left:1px solid #ececec}
.abs{position:absolute}

.brand{position:absolute;display:flex;align-items:center;gap:5px;white-space:nowrap}
.brand__square{width:12px;height:12px;background:var(--accent)}
.brand__name{font-family:"Open Sans",Arial,sans-serif;font-size:8px;font-weight:700;color:var(--green-dark)}

.contact{font-size:6px;color:var(--ink)}
.contact strong{display:block;font-family:"Libre Baskerville",Georgia,serif;font-style:italic;font-size:8px;color:var(--green-dark)}

.title{font-family:"Libre Baskerville",Georgia,serif;font-weight:700;color:var(--green)}
.h-caps{font-family:"Libre Baskerville",Georgia,serif;font-weight:700;font-size:5.6px;color:var(--green);text-transform:uppercase;margin:3px 0 2px}
.h-sub{font-family:"Libre Baskerville",Georgia,serif;font-weight:700;font-size:5.6px;color:var(--green);margin:3px 0 2px}
.body{font-size:3.7px;line-height:1.45;color:var(--ink);margin-bottom:2px}
.body--italic{font-style:italic;font-weight:700;color:var(--green)}
.call{font-family:"Libre Baskerville",Georgia,serif;font-weight:700;font-size:6.3px;color:var(--green);text-align:center;line-height:1.3}

.sky{background:var(--sky)}
.sky-soft{background:var(--sky-soft)}
.footer-box{position:absolute;background:var(--green-dark);color:#fff;text-align:center;font-size:5.5px;display:flex;flex-direction:column;justify-content:center}
.footer-box strong{font-family:"Libre Baskerville",Georgia,serif;font-style:italic;font-size:7.5px;margin-top:2px}

.photo{position:absolute}
.ph-stadium{background:linear-gradient(180deg,#1c2a4a 0%,#2f4f86 45%,#c98a4e 70%,#8a5b36 100%)}
.ph-runner{background:linear-gradient(135deg,#6b7d8f,#b8b0a8 60%,#c8322e)}
.ph-warm{background:linear-gradient(160deg,#3a2d26,#a97a5a 55%,#d1a57c)}
.ph-earth{background:linear-gradient(160deg,#5c5446,#b89a76 55%,#7e6a55)}
.ph-group{background:linear-gradient(90deg,#5a3d2c,#b9806a 40%,#c94c4c 60%,#e0c2a8)}
.ph-sunset{background:linear-gradient(180deg,#5d6f86 0%,#c99a5e 45%,#f2c66b 60%,#6d6b3c 85%,#3e4222 100%)}
.ph-mosaic{background:linear-gradient(135deg,#4a3326,#c5905e 30%,#6c6a67 45%,#d4c8b6 55%,#2f5f77 70%,#a62c2c 85%,#b7906e)}
.ph-women{background:linear-gradient(90deg,#3a2f2a,#a98c78 40%,#6b6f9a 70%,#e8e1d8)}
</style>
</head>
<body>

<section class="spread spread--left">
  <article class="panel">
    <div class="brand" style="left:14px;top:20px"><span class="brand__square"></span><span class="brand__name">Harvest Trust</span></div>
    <p class="contact abs" style="left:150px;top:18px">To learn more, email Daniel Reed at<strong>dreed@harvesttrust.org</strong></p>

    <div class="abs sky" style="left:10px;top:70px;width:114px;height:56px"></div>
    <h1 class="title abs" style="left:22px;top:80px;font-size:17px;line-height:1.15">The<br>Final Lap</h1>
    <div class="photo ph-stadium" style="left:124px;top:64px;width:136px;height:60px" role="img" aria-label="Photo area: runners on a lit stadium track at night"></div>

    <p class="body abs" style="left:10px;top:132px;width:254px">Every year, a great city marathon runs through the streets of its host city. The final lap always ends in the stadium. At the end of the race, the runners burst into the stadium for the final lap, and the crowd rises to its feet in celebration of a long journey. For 2,000 years, the church has been running a marathon mission to fulfil the Great Commission to make disciples of all nations. But now we have come into the stadium. We are on the final lap, and the crowd is standing and cheering!</p>

    <div class="abs sky" style="left:10px;top:170px;width:82px;height:124px;padding:4px">
      <h3 class="h-caps">Sprinting to the Finish</h3>
      <p class="body">In his second letter, the Apostle Peter exhorts believers to hasten the coming of the day of God. As the end of the race draws near, believers everywhere are joining the effort to finish the task.</p>
      <h4 class="h-sub">You can be part of the sprint to the finish.</h4>
      <p class="body">Partner with Harvest Trust and finance the ministries now taking the gospel for the first time to those still unreached people groups. Your investment helps hasten the coming of the day of God. In 2019, our partners took the gospel to 233 people groups in 35 countries.</p>
    </div>
    <div class="photo ph-runner" style="left:10px;top:302px;width:82px;height:100px" role="img" aria-label="Photo area: sprinter crossing the finish line"></div>

    <div class="abs" style="left:100px;top:170px;width:166px">
      <h3 class="h-caps">The Finish Line</h3>
      <p class="body">Jesus himself defined the finish line when he said, "This gospel of the kingdom will be preached in the whole world as a testimony to all nations, and then the end will come."</p>
      <h4 class="h-sub">When will the Race End?</h4>
      <p class="body body--italic">Jesus said, when the gospel has been proclaimed to "all nations."</p>
      <p class="body">In the Bible, the word "nations" refers to people groups of people who share a common ethnicity, culture, and language. Amazingly, there are about 12,000 of these "nations" around the world, and Jesus commanded us to make disciples in all of them.</p>
      <p class="body">Today there are still about 200 people groups around the world that have never heard the gospel. Most of these remaining groups are small and located in remote or difficult places. But now we can know who and where they are. By God's grace it is possible for us to engage every one of them with the gospel within the next 3 years.</p>
      <p class="body" style="text-align:center;font-weight:700;font-size:4.3px;margin-top:4px">In other words, after a long race, we're on the final lap!</p>
      <p class="call" style="margin-top:6px">Join us as we invest to make disciples in<br>"all nations" by 2022.</p>
    </div>
    <div class="footer-box" style="left:100px;top:358px;width:174px;height:42px">To learn more, email Daniel Reed at<strong>dreed@harvesttrust.org</strong></div>
  </article>

  <article class="panel">
    <div class="photo ph-warm" style="left:8px;top:10px;width:66px;height:84px" role="img" aria-label="Photo area: person from an unreached people group"></div>
    <div class="photo ph-earth" style="left:74px;top:10px;width:66px;height:84px" role="img" aria-label="Photo area: person from an unreached people group"></div>
    <div class="brand" style="left:158px;top:28px"><span class="brand__square"></span><span class="brand__name">Harvest Trust</span></div>

    <div class="abs sky" style="left:0;top:94px;width:150px;height:258px;padding:8px 10px 4px">
      <h3 class="h-caps">Where Do We Stand?</h3>
      <p class="body">Today, there are still about 200 people groups who have never heard the gospel. Most of these groups are small and located in remote or difficult places. These remaining "unengaged" people groups have no known believers.</p>
      <p class="body">But now that we know who and where these groups are, by God's grace it is possible that we could engage every one of them with the gospel within the next 3 years.</p>
      <p class="body body--italic" style="font-size:4.2px">In other words, we can finish the Great Commission!</p>
      <h3 class="h-caps" style="margin-top:6px">Hastening His Coming</h3>
      <p class="body">The Bible says that believers ought to live holy and godly lives, looking for and hastening the coming of the day of God. It also says that day will not come until the gospel has been preached to all nations. So, how can we hasten the day of his coming? By finishing the task given us to make disciples of all nations.</p>
      <h4 class="h-sub" style="font-size:6.3px;margin-top:5px">You can make that happen.</h4>
      <p class="body">Partner with Harvest Trust and finance the ministries now taking the gospel for the first time to those last remaining people groups. Your investment will hasten the coming of the day of God. In 2019, our partners helped take the gospel to 233 people groups in 35 countries.</p>
    </div>

    <h2 class="title abs" style="left:158px;top:96px;font-size:15px;line-height:1.12">Finishing<br>The Great<br>Commission</h2>
    <p class="body abs" style="left:158px;top:150px;width:108px">Before Jesus ascended into heaven, He commanded his apostles, "Go and make disciples of all nations." For more than 2,000 years the church has been working to fulfil this Great Commission. But now, for the first time in history, our generation has the real opportunity to finish it in our lifetimes.</p>
    <div class="photo ph-group" style="left:158px;top:190px;width:108px;height:50px" role="img" aria-label="Photo area: three villagers smiling together"></div>
    <div class="abs sky-soft" style="left:150px;top:248px;width:124px;height:54px;padding:4px 8px">
      <h3 class="h-caps">It's About Nations</h3>
      <p class="body">In the Bible the word "nations" refers to people groups who share a common ethnicity, culture, and language. There are about 12,000 of these groups throughout the world, and the Great Commission commands us to make disciples in every one of them.</p>
    </div>
    <p class="call abs" style="left:156px;top:308px;width:112px">Join us as we invest to make disciples in "all nations" by 2022.</p>

    <div class="brand" style="left:10px;top:374px"><span class="brand__square"></span><span class="brand__name">Harvest Trust</span></div>
    <div class="footer-box" style="left:100px;top:358px;width:174px;height:42px">To learn more, email Daniel Reed at<strong>dreed@harvesttrust.org</strong></div>
  </article>
</section>

<section class="spread spread--right">
  <article class="panel">
    <div class="brand" style="left:12px;top:34px"><span class="brand__square"></span><span class="brand__name">Harvest Trust</span></div>
    <h2 class="title abs" style="left:110px;top:24px;font-size:12.5px;line-height:1.2;text-align:center;width:150px">HASTENING HIS<br>COMING</h2>
    <p class="body abs" style="left:12px;top:68px;width:262px">In his second letter the Apostle Peter asks what kind of people should believers be? He answers, "We ought to live holy and godly lives, looking for and hastening the coming of the day of God." But how can we do that? How is it possible to hasten that day?</p>
    <h3 class="title abs" style="left:12px;top:88px;font-size:9.5px">"AND THEN THE END WILL COME"</h3>
    <p class="body abs" style="left:12px;top:104px;width:262px">When Jesus' disciples asked Him, "What will be the sign of your coming and of the end of the age?" He replied, "This gospel of the kingdom will be preached in the whole world as a testimony to all nations, and then the end will come."</p>

    <div class="abs sky" style="left:0;top:122px;width:279px;height:108px"></div>
    <div class="abs" style="left:12px;top:126px;width:130px">
      <h3 class="h-sub" style="font-size:6.5px;line-height:1.3">When will Jesus return?<br>He said, only after gospel has been preached to "all nations."</h3>
      <p class="body">In the Bible, the word "nations" refers to people groups who share a common ethnicity, culture, and language. There are about 12,000 of these "nations" in the world, and Jesus commanded his church to preach the gospel to all of them. Today, 200 groups still have no believer.</p>
      <p class="body body--italic">After 2000 years, let's hasten that day all heard!</p>
    </div>
    <div class="photo ph-sunset" style="left:148px;top:130px;width:124px;height:90px" role="img" aria-label="Photo area: sun breaking through clouds over a field"></div>

    <div class="abs" style="left:12px;top:236px;width:262px">
      <h3 class="h-caps" style="font-size:6.5px">Finishing the Task</h3>
      <p class="body">So how can we hasten the coming of the day of God? By accelerating the work that is promised and preparing the way for His return. Today we know where the last unengaged groups are and who could reach them. By God's grace, it is possible that we can engage all of them with the gospel within the next 3 years.</p>
      <h3 class="h-caps" style="font-size:6.5px;margin-top:6px">You can make that happen.</h3>
      <p class="body">Partner with Harvest Trust and finance the missionaries who are taking the gospel for the first time to those last remaining people groups. Your investment will "hasten the coming of the day of God" by accelerating the effort to make disciples in every nation. In 2019, our partners helped take the gospel to 233 people groups in 35 countries.</p>
    </div>
    <div class="brand" style="left:12px;top:366px"><span class="brand__square"></span><span class="brand__name">Harvest Trust</span></div>
    <div class="footer-box" style="left:98px;top:350px;width:181px;height:44px">To learn more, email Daniel Reed at<strong>dreed@harvesttrust.org</strong></div>
  </article>

  <article class="panel">
    <div class="brand" style="left:12px;top:34px"><span class="brand__square"></span><span class="brand__name">Harvest Trust</span></div>
    <div class="photo ph-mosaic" style="left:172px;top:10px;width:99px;height:80px" role="img" aria-label="Photo area: grid of six photos of people from many nations"></div>
    <h2 class="title abs" style="left:12px;top:62px;font-size:15px;line-height:1.1">GOD'S HEART<br><span style="font-size:10px">FOR THE NATIONS</span></h2>

    <div class="abs" style="left:11px;top:108px;width:124px">
      <p class="body">From beginning to end the Bible reveals God's heart for the nations. In Genesis, God promises Abraham, "through your offspring all nations of the earth will be blessed."</p>
      <p class="body">The Psalms prophesy that "all the nations you have made will come and worship before you, Lord."</p>
      <p class="body">In Isaiah, God promises the Messiah, "I will make you a light to the nations, that my salvation may reach to the ends of the earth."</p>
      <p class="body">Daniel sees "one like a son of man" who "was given authority, glory and sovereign power; all nations and peoples of every language worshiped him."</p>
      <p class="body">In Matthew, Jesus commands his apostles to</p>
    </div>
    <div class="abs" style="left:142px;top:108px;width:126px">
      <p class="body">"Go and make disciples of all nations." And he links his return to the completion of that task, saying, "This gospel of the kingdom will be preached in the whole world as a testimony to all nations, and then the end will come."</p>
      <p class="body">In Revelation, John sees a great multitude that no one could number, from every nation, tribe, people and language, standing before the throne.</p>
      <p class="body">In the Bible, the word "nations" refers to people groups who share a common ethnicity, culture, and language. There are more than 12,000 of these nations around the world, and God has promised that every one will be included in His Kingdom.</p>
    </div>

    <div class="abs sky" style="left:0;top:230px;width:279px;height:72px"></div>
    <h3 class="title abs" style="left:11px;top:234px;font-size:9.5px;line-height:1.15">FINISHING THE<br>TASK</h3>
    <div class="photo ph-women" style="left:11px;top:260px;width:84px;height:38px" role="img" aria-label="Photo area: group of women from several nations"></div>
    <div class="abs" style="left:142px;top:234px;width:126px">
      <p class="body">Today, there are still 200 nations not yet represented in God's Kingdom. No one has ever proclaimed the gospel to these unengaged people groups, and there are no believers among them.</p>
      <p class="body">Most of these groups are small and located in remote or difficult places. But now, we can know who and where they are. By God's grace, we can engage every one of them with the gospel within the next 3 years.</p>
    </div>
    <div class="abs" style="left:11px;top:306px;width:258px">
      <h4 class="h-sub" style="font-size:6.3px">You can make that happen.</h4>
      <p class="body">Partner with Harvest Trust and finance the missionaries who are taking the gospel for the first time to those last remaining people groups. Your investment will "hasten the coming of the day of God" by accelerating the effort to make disciples in every nation. In 2019, our partners helped take the gospel to 233 people groups in 35 countries.</p>
    </div>
    <div class="brand" style="left:11px;top:366px"><span class="brand__square"></span><span class="brand__name">Harvest Trust</span></div>
    <div class="footer-box" style="left:98px;top:350px;width:181px;height:44px">To learn more, email Daniel Reed at<strong>dreed@harvesttrust.org</strong></div>
  </article>
</section>

</body>
</html>
```